Brevard médico-conseils - word template

We are dooing lot of médical report from word document. We dont print the text on a stationnary. We are producting the report and save it in pdf. So I need à word template. I want something more than just hard the logo. I would like the look of a stationnary in the word template.

I put an exemple of report. But the final don't have to look that way. Propose something more acurate.
After that I will need a business card.

Industry/Entity Type

Medical

Requirements
Must have
• We have to do a design that integrate are logo and color. You have the file in the project.
• The wrihting beteen the title must be in times new roman.
Nice to have
• We have 2 offices:
• Québec (Building Val-Doré) 512, ave des Tilleuls, local 210, G2K 4P7 T.418 555-7142 T.418 555-7189
• St-Romuald (Building Carrefour Marbel-Les quais) 2350, boul. des Érables, local 305, G7B 2N4. T.418 555-0263 F.418 555-0398
• Mail: info@BrevardMC.com and expertise@BrevardMC.com
• Web: www.BrevardMC.com
• For now you can type www.PTRV.ca to acces the web site.
Should not have
• The same look that the exemple. Because I want to upgrade the look of the company.

```html
<!DOCTYPE html>
<html lang="fr">
<head>
<meta charset="utf-8">
<title>Rapport complémentaire du médecin – Brevard médico-conseils</title>
<link rel="stylesheet" href="https://fonts.googleapis.com/css2?family=Tinos:ital,wght@0,400;0,700;1,400;1,700&family=Arimo:wght@400;700&family=Open+Sans:wght@400;700&display=swap">
<style>
  :root {
    --brand-blue: #2a7de1;
    --brand-teal: #3aa2ad;
    --ink: #111111;
    --rule: #555555;
    --paper: #ffffff;
  }
  * { margin: 0; padding: 0; box-sizing: border-box; }
  html, body { width: 927px; height: 1200px; overflow: hidden; background: var(--paper); }
  .page { position: relative; width: 927px; height: 1200px; font-family: "Tinos", "Times New Roman", serif; color: var(--ink); font-size: 18px; line-height: 21px; }
  .abs { position: absolute; }

  .letterhead { top: 0; left: 0; width: 927px; height: 154px; background: var(--brand-blue); }
  .services { left: 109px; top: 58px; list-style: none; font-family: "Open Sans", Arial, sans-serif; font-size: 12px; line-height: 17px; color: #fff; }
  .services li:first-child { padding-left: 4px; }
  .brand { right: 18px; top: 74px; display: flex; align-items: center; gap: 14px; color: #fff; font-family: "Arimo", Arial, sans-serif; font-size: 36px; font-weight: 400; white-space: nowrap; }
  .brand-mark { width: 50px; height: 60px; background: #fff; }

  .report-title { top: 228px; left: 0; width: 927px; text-align: center; color: var(--brand-teal); font-weight: 700; font-size: 21px; line-height: 24px; }

  .section-label { font-family: "Arimo", Arial, sans-serif; font-weight: 700; color: var(--brand-teal); font-size: 20px; line-height: 22px; transform: rotate(-90deg); transform-origin: center; white-space: nowrap; text-align: center; width: 200px; margin-left: -100px; }
  .section-rule { left: 151px; width: 1px; background: var(--rule); }

  .field { font-weight: 700; font-style: italic; }
  .field .colon { font-weight: 400; }
  .divider { top: 430px; left: 0; width: 927px; text-align: center; color: var(--brand-teal); font-size: 14px; }
  .bullets { list-style: none; }
  .bullets li { position: relative; padding-left: 26px; }
  .bullets li::before { content: ""; position: absolute; left: 5px; top: 8px; width: 6px; height: 6px; border-radius: 50%; background: var(--ink); }
  .rx-link { color: var(--brand-teal); text-decoration: underline; }

  .signoff { font-weight: 700; }

  .footer { top: 1120px; left: 0; width: 927px; height: 80px; background: var(--brand-blue); color: #fff; font-family: "Arimo", Arial, sans-serif; font-size: 13.5px; line-height: 21px; }
  .footer .offices { left: 108px; top: 7px; }
  .footer .phones { right: 12px; top: 7px; text-align: left; }
</style>
</head>
<body>
<div class="page">
  <header class="letterhead abs">
    <ul class="services abs">
      <li>Expertise</li><li>Service santé</li><li>Pré-emploi</li><li>Bilan exécutif</li><li>Vaccination</li>
    </ul>
    <div class="brand abs"><span class="brand-mark"></span>Brevard médico-conseils</div>
  </header>

  <h1 class="report-title abs">RAPPORT COMPLÉMENTAIRE DU MÉDECIN</h1>

  <div class="section-rule abs" style="top:277px;height:134px"></div>
  <div class="section-label abs" style="left:131px;top:332px">Information</div>
  <div class="field abs" style="left:160px;top:277px">NO. DE DOSSIER</div>
  <div class="abs" style="left:382px;top:277px">#7101</div>
  <div class="field abs" style="left:160px;top:298px">EMPLOYEUR <span class="colon">:</span></div>
  <div class="abs" style="left:382px;top:298px">HARLOW</div>
  <div class="field abs" style="left:160px;top:319px">EMPLOYÉ(E) <span class="colon">:</span></div>
  <div class="abs" style="left:382px;top:319px">toto</div>
  <div class="field abs" style="left:160px;top:356px">POSTE <span class="colon">:</span></div>
  <div class="abs" style="left:382px;top:356px">Marchandiseur</div>
  <div class="field abs" style="left:160px;top:391px">DATE DE L’EXAMEN</div>
  <div class="abs" style="left:382px;top:391px">27/03/2015</div>

  <div class="divider abs">***</div>

  <div class="section-rule abs" style="top:474px;height:382px"></div>
  <div class="section-label abs" style="left:131px;top:653px">Médical</div>
  <div class="field abs" style="left:160px;top:476px">ANTÉCÉDENTS <span class="colon">:</span></div>
  <ul class="bullets abs" style="left:414px;top:476px">
    <li>Poids fort</li><li>Allergies : Pénicilline</li>
  </ul>
  <p class="abs" style="left:385px;top:541px"><b>Symptômes :</b> Le candidat n'a pas identifié de symptôme.</p>
  <p class="abs" style="left:385px;top:582px;width:440px"><b>Maladies:</b> Le candidat n'a JAMAIS manqué du travail dû à l'une des maladies identifiées ici-bas.</p>
  <ul class="bullets abs" style="left:414px;top:625px">
    <li style="padding-left:25px">depuis novembre 2014 – tube oreille droite.</li>
  </ul>
  <div class="field abs" style="left:160px;top:667px">EXAMEN PHYSIQUE</div>
  <div class="abs" style="left:385px;top:667px">Normal<br>SAUF : Excès de poids</div>
  <div class="field abs" style="left:160px;top:730px">RECOMMANDATIONS <span class="colon">:</span></div>
  <div class="abs" style="left:385px;top:730px"><b>Apte au travail</b></div>
  <ul class="bullets abs" style="left:414px;top:752px"><li>16 - Pas de bruits, protection exigée</li></ul>
  <div class="field abs" style="left:160px;top:835px">DOSSIER DE CSST <span class="colon">:</span></div>
  <div class="abs" style="left:385px;top:835px">Aucun</div>

  <div class="section-rule abs" style="top:875px;height:78px"></div>
  <div class="section-label abs" style="left:131px;top:903px">RX</div>
  <div class="rx-link abs" style="left:160px;top:877px">(Pour la description exacte – voir le rapport de radiologie)</div>
  <div class="field abs" style="left:160px;top:912px">RX-LOMBAIRE</div>
  <div class="abs" style="left:458px;top:912px">PAS de restriction</div>
  <div class="abs" style="left:613px;top:912px">Léger pincement</div>

  <div class="signoff abs" style="left:109px;top:996px">Médecin:<br>Rédaction:<br>Validation:</div>
  <div class="abs" style="left:323px;top:996px">Dr Marc Vallières<br>Sophie Tremblin<br>MTR</div>
  <div class="abs" style="left:591px;top:1038px">Date: 27/03/2015</div>

  <footer class="footer abs">
    <div class="offices abs">
      Québec (Building Val-Doré) 512, ave des Tilleuls, local 210, G2K 4P7<br>
      St-Romuald (Building Carrefour Marbel-Les quais) 2350, boul. des Érables, local 305, G7B 2N4.<br>
      Mail : info@BrevardMC.com and expertise@BrevardMC.com &nbsp; | &nbsp; Web : www.BrevardMC.com
    </div>
    <div class="phones abs">
      T.418 555-7142 T.418 555-7189<br>
      T.418 555-0263 &nbsp;F.418 555-0398
    </div>
  </footer>
</div>
</body>
</html>
```